Swerve (nightclub flyer)

Nightclub flyer, guaranteed project. Text below (and please use logos, large):

SWERVE PRESENTS:

KORVEN (LOGO) B2B MARTY DELANO (LOGO)

+TOBBI RASK (smaller text)

10/26/17

2284 ELM LANE SACRAMENTO CA
21+ 10PM-2AM

HOUSE/TECHNO

A VELVET ORCHID ENTERTAINMENT (LOGO) PRODUCTION

Target Market(s)

House/Electronic Music Lovers

Industry/Entity Type

Night Club

Font styles to use
Sans Serif

Colors

Designer to choose colors to be used in the design.

Requirements
Must have
• Large logos for the dj names, or large block letter dj names (logos not necessary if it looks better without. But KORVEN b2b MARTY DELANO large and TOBBI RASK smaller on separate line
Nice to have
• Can include a classy female model but nothing cheesy or too sexy

```html
<!DOCTYPE html>
<html lang="en">
<head>
<meta charset="utf-8">
<title>Swerve presents Korven</title>
<link rel="stylesheet" href="https://fonts.googleapis.com/css2?family=Tinos:wght@700&family=Russo+One&family=Montserrat:wght@400;500&family=Oswald:wght@500&family=Quicksand:wght@400;500&display=swap">
<style>
  :root {
    --ink: #0b0b0d;
    --pink: #e8198c;
    --blue: #1e8fe0;
    --sky: #2aa6ec;
    --yellow: #ffec00;
    --white: #ffffff;
    --red: #d42a1e;
  }
  * { margin: 0; padding: 0; box-sizing: border-box; }
  html, body { width: 849px; height: 1200px; overflow: hidden; background: var(--ink); }
  .flyer {
    position: relative;
    width: 849px;
    height: 1200px;
    background: var(--ink);
    overflow: hidden;
    text-align: center;
  }
  .crowd-photo {
    position: absolute;
    left: 0; top: 0;
    width: 849px; height: 440px;
    background:
      radial-gradient(ellipse at 50% 0%, #ff86c8 0%, rgba(255,134,200,0) 60%),
      linear-gradient(180deg, #f0369a 0%, #c41877 40%, #5a0a38 75%, var(--ink) 100%);
  }
  .stripes { position: absolute; left: 0; top: 0; }
  .line { position: absolute; left: 0; width: 849px; }
  .presenter {
    top: 40px;
    font-family: "Tinos", serif;
    font-weight: 700;
    font-size: 38px;
    color: var(--white);
    letter-spacing: 1px;
  }
  .headliner {
    top: 82px;
    font-family: "Russo One", sans-serif;
    font-size: 128px;
    color: var(--blue);
    letter-spacing: 4px;
    line-height: 1;
  }
  .b2b {
    position: absolute;
    left: 369px; top: 238px;
    width: 110px; height: 110px;
    border-radius: 50%;
    background: var(--ink);
    border: 3px solid var(--white);
    font-family: "Montserrat", sans-serif;
    font-weight: 500;
    font-size: 34px;
    line-height: 104px;
    color: var(--white);
    letter-spacing: 2px;
  }
  .co-headliner {
    top: 362px;
    font-family: "Oswald", sans-serif;
    font-weight: 500;
    font-size: 106px;
    line-height: 1.1;
    color: var(--yellow);
    letter-spacing: 3px;
  }
  .guest {
    top: 492px;
    font-family: "Montserrat", sans-serif;
    font-weight: 400;
    font-size: 46px;
    color: var(--white);
    letter-spacing: 3px;
  }
  .date {
    top: 590px;
    font-family: "Quicksand", sans-serif;
    font-weight: 400;
    font-size: 88px;
    color: var(--sky);
    transform: rotate(-5deg);
    letter-spacing: 2px;
  }
  .venue {
    top: 722px;
    font-family: "Quicksand", sans-serif;
    font-weight: 500;
    font-size: 54px;
    line-height: 1.05;
    color: var(--white);
    transform: rotate(-5deg);
    letter-spacing: 2px;
  }
  .entry {
    top: 862px;
    font-family: "Quicksand", sans-serif;
    font-weight: 500;
    font-size: 80px;
    color: var(--pink);
    transform: rotate(-5deg);
    letter-spacing: 1px;
  }
  .genre {
    top: 1000px;
    font-family: "Quicksand", sans-serif;
    font-weight: 500;
    font-size: 62px;
    color: var(--white);
    transform: rotate(-2deg);
    letter-spacing: 1px;
  }
  .credit {
    top: 1118px;
    font-family: "Quicksand", sans-serif;
    font-weight: 500;
    font-size: 20px;
    color: var(--white);
    letter-spacing: 1px;
  }
</style>
</head>
<body>
<main class="flyer">
  <div class="crowd-photo" role="img" aria-label="Crowd of clubbers with raised hands under pink stage light"></div>

  <svg class="stripes" width="849" height="1200" viewBox="0 0 849 1200" aria-hidden="true">
    <g class="stripes-left">
      <polygon points="0,960 0,978 240,1200 214,1200" fill="var(--pink)"/>
      <polygon points="0,995 0,1016 200,1200 172,1200" fill="var(--red)"/>
      <polygon points="0,1032 0,1052 162,1200 136,1200" fill="var(--blue)"/>
    </g>
    <g class="stripes-right">
      <polygon points="690,770 849,862 849,882 680,786" fill="var(--blue)"/>
      <polygon points="675,795 849,896 849,920 665,812" fill="var(--red)"/>
      <polygon points="660,822 849,932 849,956 650,838" fill="var(--pink)"/>
    </g>
  </svg>

  <p class="line presenter">SWERVE PRESENTS:</p>
  <h1 class="line headliner">KORVEN</h1>
  <p class="b2b">B2B</p>
  <h2 class="line co-headliner">MARTY DELANO</h2>
  <p class="line guest">+TOBBI RASK</p>

  <p class="line date">26 October 17</p>
  <p class="line venue">2284 ELM LANE<br>SACRAMENTO CA</p>
  <p class="line entry">21+ 10PM-2AM</p>
  <p class="line genre">HOUSE/TECHNO</p>
  <p class="line credit">A VELVET ORCHID ENTERTAINMENT PRODUCTION</p>
</main>
</body>
</html>
```